依頼詳細
・O P E Nチラシ作成
・地図の作成

開店前に近隣にチラシを配布する予定です、そのチラシのデザイン作成をお願いいたします。
封筒に入れて配布する事を考えており、封書を開けて見た時に期待感のある、高級感の漂うデザインをお願いします。
オープン日時が7月20日となっているのですが、緊急事態宣言や蔓延防止の関係で日時の変更がある場合対応お願いします
最寄駅から店舗までの地図を作成して下さい。

高級料理店・コースのみのお店ですので、高級感、清潔感、重厚感、のあるチラシ希望です。
参考資料として、現在店頭に貼っているポスターや近隣店舗の地図のデータを添付いたします。
記載項目
店名・住所・電話番号・地図・定休日・

サイズ
A4
ページ数
片面
希望イメージ
シンプル 複雑
単色 カラフル
暗い 明るい
日常 高級
遊び心 厳粛
未来的 伝統的
女性的 男性的
希望する色
赤系、青系、無彩色系
納品ファイル
• イラストレーター形式 (.ai)
補足説明
完成品はA4のZ折り、ハルナギ堂で印刷予定です。よろしくお願いいたします。
ロゴのデータを追加して貼り付けました。
料理データ、Chefの画像等も追加で添付してまいりますが、
現在フォトグラファーがレタッチをしておりますので、データ納品後に差し替えをお願いいたします。
料理画像とシェフの画像を追加いたします。

Photograph クドウ ユリエ
レタッチ後の料理画像とシェフの画像を添付いたします。

どうぞよろしくお願いいたします。

封入から取り出した際の期待感やイメージがお店のイメージと合っていた。

短い期間の中での募集にも関わらず、多くのご応募ありがとうございました。
新たな提案が来るたびに、スタッフ同士で何度も検討を重ねました。
自分達だけでは、気が付かなかったアイディアや発見もあり、今後の参考になりました。
本当に皆様ありがとうございました。

```html
<!DOCTYPE html>
<html lang="ja">
<head>
<meta charset="utf-8">
<title>Marée Douce Grand Open</title>
<link rel="stylesheet" href="https://fonts.googleapis.com/css2?family=Playfair+Display:ital,wght@0,400;1,400&family=Great+Vibes&family=Shippori+Mincho:wght@400;600;700&display=swap">
<style>
:root{
  --navy:#141b2b;
  --navy-deep:#0d1220;
  --gold:#c9a55a;
  --ink:#2a2a2a;
  --muted:#6b6b6b;
  --paper:#ffffff;
  --line:#d9d9d9;
  --red:#c4272f;
  --blue:#1f3f8f;
}
*{margin:0;padding:0;box-sizing:border-box}
html,body{width:849px;height:1200px;overflow:hidden;background:var(--paper)}
body{position:relative;font-family:"Shippori Mincho",serif;color:var(--ink)}
.abs{position:absolute}

.hero{left:0;top:0;width:849px;height:318px;background:var(--navy)}
.hero-photo{left:0;top:0;width:430px;height:318px;background:radial-gradient(ellipse at 40% 55%,#6b2a22 0%,#3b1a18 40%,var(--navy) 78%)}
.grand-open{left:445px;top:8px;font-family:"Playfair Display",serif;font-size:58px;line-height:1;color:var(--gold)}
.open-date{left:520px;top:74px;color:var(--gold);font-family:"Playfair Display",serif;font-size:15px;line-height:1}
.open-date b{font-size:32px;font-weight:400;margin:0 6px}
.tagline{left:445px;top:112px;color:#fff;font-size:24px;line-height:1.45;font-weight:600}
.logo-box{left:650px;top:108px;width:120px;height:72px;background:#fff;display:flex;align-items:center;justify-content:center;gap:8px}
.logo-box .dot{width:22px;height:22px;border-radius:50%;background:var(--navy)}
.logo-box span{font-size:13px;color:var(--navy);font-weight:600}
.hero-note{left:445px;top:196px;width:380px;color:#ddd;font-size:10px;line-height:1.75}

.feature-title{left:30px;top:334px;font-size:24px;font-weight:700;color:var(--navy);line-height:1.2}
.tricolor{left:30px;top:368px;width:380px}
.feature-body{left:30px;top:382px;width:385px;font-size:11px;line-height:1.8}
.prices{left:110px;top:478px;font-size:12px;line-height:1.7}
.flag-bar{left:0;top:520px;width:8px;height:150px}
.menu{left:60px;top:528px;width:320px;font-size:9.5px;line-height:1.8;color:var(--muted);text-align:center}
.dish-photo{left:430px;top:318px;width:419px;height:290px;background:linear-gradient(135deg,#e9e5df 0%,#b58a6a 45%,#7a4a3a 70%,#ebe7e2 100%)}
.script-name{left:620px;top:604px;font-family:"Great Vibes",cursive;font-size:34px;line-height:1.2;color:var(--navy)}
.story{left:560px;top:652px;width:270px;font-size:10px;line-height:1.75}

.info{left:25px;top:752px;width:190px}
.info .name{font-family:"Playfair Display",serif;font-size:26px;color:var(--navy);line-height:1.2}
.info .kana{font-size:13px;margin:4px 0 10px;letter-spacing:2px}
.info p{font-size:10px;line-height:1.7}
.info .tel{font-size:15px;font-weight:600}
.map{left:212px;top:752px;width:210px;height:180px;background:#f1f1f1;border:1px solid var(--line)}
.chef-photo{left:430px;top:720px;width:419px;height:310px;background:linear-gradient(180deg,#d6d6d6 0%,#8a8a8a 55%,#3a3a3a 100%)}

.profile-rule{left:20px;top:1045px;width:809px;height:1px;background:var(--line)}
.profile-label{left:25px;top:1085px;font-family:"Great Vibes",cursive;font-size:24px;line-height:1.2;color:var(--navy)}
.profile-text{left:150px;top:1065px;width:670px;font-size:9.5px;line-height:1.8;color:var(--ink)}
.credit{right:20px;top:1172px;font-size:9px;color:var(--muted)}
</style>
</head>
<body>
<div class="abs hero"></div>
<div class="abs hero-photo" role="img" aria-label="Plated red meat dish with sauce on a dark table"></div>
<div class="abs grand-open">Grand Open</div>
<div class="abs open-date">2021<b>7/20</b>Tuesday</div>
<div class="abs tagline">桜ヶ丘に愛される<br>フレンチを。</div>
<div class="abs logo-box"><div class="dot"></div><span>Marée Douce</span></div>
<p class="abs hero-note">駅前にフレンチレストラン「Marée Douce」がオープンします。季節の食材を活かしたコース料理で、大切な日のひとときを上質な空間とともにお届けいたします。皆様のご来店を心よりお待ちしております。</p>

<h2 class="abs feature-title">クラシックとモダンの融合</h2>
<svg class="abs tricolor" height="4" viewBox="0 0 380 4"><rect width="126" height="4" fill="var(--blue)"/><rect x="127" width="126" height="4" fill="#e5e5e5"/><rect x="254" width="126" height="4" fill="var(--red)"/></svg>
<p class="abs feature-body">お客様のご要望にお応えする、最高の料理と空間を。伝統的なフランス料理の技法を大切にしながら、現代の感性を取り入れた一皿をご提供いたします。記念日や会食など、特別な時間をゆっくりとお過ごしください。完全予約制のコースのみのご案内となります。</p>
<p class="abs prices">ランチ　3,000円～5,000円の2種<br>ディナー 7,000円～9,000円の2種</p>
<svg class="abs flag-bar" viewBox="0 0 8 150" preserveAspectRatio="none"><rect width="8" height="50" fill="var(--blue)"/><rect y="50" width="8" height="50" fill="#e5e5e5"/><rect y="100" width="8" height="50" fill="var(--red)"/></svg>
<p class="abs menu">アミューズ<br>季節の前菜 ～ 旬の野菜とともに<br>本日のスープ<br>魚料理 ～ ソース・ブールブラン<br>肉料理 ～ 仔羊のロースト<br>デザート<br>コーヒー・紅茶</p>
<div class="abs dish-photo" role="img" aria-label="Roasted rack of lamb on a white plate"></div>
<div class="abs script-name">Marée Douce</div>
<p class="abs story">フランス語で「穏やかな潮」を意味する店名には、訪れる方の心がほどける場所でありたいという想いを込めました。一皿ごとに丁寧に仕上げた料理をお楽しみください。</p>

<div class="abs info">
  <div class="name">Marée Douce</div>
  <div class="kana">マレドゥース</div>
  <p>〒156-0000 東京都桜ヶ丘市中町1-2-3</p>
  <p class="tel">TEL.03-5550-2718</p>
  <p>Lunch 11:30-15:00（L.O.14:00）<br>Dinner 18:00-22:00（L.O.21:00）</p>
  <p>定休日 月曜日・第二火曜日</p>
</div>
<div class="abs map" role="img" aria-label="Map from the nearest station to the restaurant"></div>
<div class="abs chef-photo" role="img" aria-label="Black and white photo of the chef plating a dish"></div>

<div class="abs profile-rule"></div>
<div class="abs profile-label">Chef Profile</div>
<p class="abs profile-text">都内のホテルで修業を重ねたのち渡仏し、各地の星付きレストランで研鑽を積む。帰国後は料理長としてフレンチの厨房を率い、2021年「Marée Douce」を開店。素材の持ち味を引き出す一皿を追求し、季節ごとに変わるコースで訪れる方を迎えている。</p>
<div class="abs credit">Photograph ミズノ サキ</div>
</body>
</html>
```